Logistics Website Design

See website https://tvarfreightglobal.com for theme and color details. Need the site to be re-done and reflect some of the designs shown in this list here: https://pinvora.com/tags/logistics-company-website

Target Market(s)

Logistics & Transportation

Industry/Entity Type

Logistics and Supply Chain

Coding

Coded - Design and coding required

Number of Pages Required

5+ page

Requirements
Must have
• Colors must match theme of logo. Looking for a sleek, interactive design.

```html
<!DOCTYPE html>
<html lang="en">
<head>
<meta charset="utf-8">
<title>Tvar Freight — Food &amp; Beverage</title>
<link rel="stylesheet" href="https://fonts.googleapis.com/css2?family=Oswald:wght@300;400;500;600;700&family=Roboto+Condensed:ital,wght@1,700&display=swap">
<style>
:root{
  --orange:#ef8560;
  --orange-deep:#e8734b;
  --opt-1:#f08c68;
  --opt-2:#e97a55;
  --opt-3:#d9704d;
  --opt-4:#c9633f;
  --ink:#1d1d1d;
  --muted:#777;
  --black:#000;
  --panel:#f4f4f4;
  --footer:#2a2a2a;
  --white:#fff;
}
*{margin:0;padding:0;box-sizing:border-box}
html,body{width:1200px;height:3773px;overflow:hidden}
body{position:relative;background:var(--white);font-family:"Oswald",sans-serif;color:var(--ink)}
.abs{position:absolute}

/* hero */
.hero{left:0;top:0;width:1200px;height:853px;background:var(--black)}
.nav{left:100px;top:25px;width:999px;height:38px;border-radius:10px;background:var(--white);overflow:hidden}
.nav-right{position:absolute;right:0;top:0;width:455px;height:38px;background:var(--orange)}
.nav a{position:absolute;top:11px;font-size:10px;font-weight:500;color:var(--ink);text-decoration:none;letter-spacing:.2px}
.nav-right a{color:var(--white)}
.nav-right a.active{background:var(--opt-2);padding:11px 8px;top:0}
.brand{left:565px;top:10px;width:74px;height:64px;border-radius:50%;background:var(--black);border:3px solid var(--orange);display:flex;align-items:center;justify-content:center}
.brand span{font-size:10px;font-weight:600;color:var(--orange);text-align:center;line-height:1.1}
.submenu{left:830px;top:64px;width:64px;height:90px;background:var(--orange);padding:4px 6px;font-size:4.5px;color:var(--white);line-height:1.3}
.submenu p{margin-bottom:6px}
.page-title{left:0;top:128px;width:1200px;text-align:center;font-size:38px;font-weight:700;color:var(--orange);letter-spacing:.5px}
.hero-photo{left:103px;top:212px;width:1002px;height:433px;border-radius:40px;background:linear-gradient(90deg,#6b6e66 0%,#4f7a34 25%,#c76a2a 45%,#e5e2da 70%,#3b4d2e 100%)}
.hero-copy{left:157px;top:706px;width:876px;font-size:19px;font-weight:300;color:var(--white);text-align:justify;text-align-last:center;line-height:1.3;letter-spacing:-.15px;word-spacing:1px}

/* capabilities */
.cap{left:95px;width:400px}
.cap h2{font-size:26px;font-weight:500;color:var(--ink);letter-spacing:-.3px}
.cap h2 em{font-style:normal;color:var(--orange)}
.cap ul{list-style:none;margin-top:10px;font-size:10px;font-weight:300;color:var(--muted);line-height:1.36}
.photo.truck{left:502px;top:875px;width:260px;height:608px;border-radius:22px;background:linear-gradient(180deg,#6b6f74 0%,#3a4a5c 45%,#2b3138 100%)}
.photo.shutter{left:782px;top:875px;width:314px;height:216px;border-radius:22px;background:linear-gradient(160deg,#c9cbcd,#7b8186 70%,#3a3f44)}
.photo.drums-a{left:782px;top:1115px;width:148px;height:217px;border-radius:20px;background:linear-gradient(180deg,#7a6d5d,#dcdcd9 50%,#a6a29a)}
.photo.drums-b{left:948px;top:1115px;width:148px;height:217px;border-radius:20px;background:linear-gradient(180deg,#6e5f4d,#d9d8d4 55%,#908b82)}
.photo.loader{left:782px;top:1354px;width:314px;height:334px;border-radius:22px;background:linear-gradient(160deg,#7c6a55,#b76a3b 45%,#4a4d50)}

/* quote */
.quote{left:0;top:1719px;width:1200px;height:969px;background:var(--panel)}
.quote-title{left:0;top:1744px;width:1200px;text-align:center;font-size:30px;font-weight:600;color:var(--ink)}
.field{height:52px;border:2px solid var(--orange);border-radius:8px;background:var(--white);font-size:17px;font-weight:400;color:#9a9a9a;padding:14px 0 0 29px}
.select{border:2px solid var(--orange);border-radius:8px;overflow:hidden;background:var(--white)}
.select .head{height:50px;font-size:17px;color:#9a9a9a;padding:14px 0 0 29px;position:relative}
.select .head svg{position:absolute;right:18px;top:20px}
.select .opt{height:33px;font-size:13px;font-weight:400;color:var(--white);padding:8px 0 0 29px}
.o1{background:var(--opt-1)}.o2{background:var(--opt-2)}.o3{background:var(--opt-3)}.o4{background:var(--opt-4)}
.message{left:264px;top:2378px;width:699px;height:193px;border-radius:8px;background:var(--orange-deep);display:flex;align-items:center;justify-content:center;font-size:20px;color:#f8b9a2}
.cta{left:498px;top:2596px;width:255px;height:54px;background:var(--orange-deep);color:var(--white);font-size:26px;display:flex;align-items:center;justify-content:center;font-weight:400}
.mission{left:0;top:2733px;width:1200px;text-align:center;font-family:"Roboto Condensed",sans-serif;font-style:italic;font-weight:700;font-size:21px;line-height:1.25;color:#2b2b2b}

/* footer */
.footer{left:0;top:2849px;width:1200px;height:293px;background:var(--footer)}
.f-brand{left:100px;top:2945px;width:66px;height:60px;border-radius:50%;border:2px solid var(--orange);display:flex;align-items:center;justify-content:center;font-size:9px;font-weight:600;color:var(--orange);text-align:center;line-height:1.1}
.f-tag{left:100px;top:3030px;font-size:12px;line-height:1.15;color:var(--white)}
.f-col{color:var(--white)}
.f-col h4{font-size:12px;font-weight:400;margin-bottom:14px;color:var(--white)}
.f-col p{font-size:8px;font-weight:300;margin-bottom:13px;color:#ddd}
.f-contact p{font-size:6px;line-height:1.25;margin-bottom:0;width:150px}
.phone{font-size:22px;font-weight:600;margin-top:20px;color:var(--white)}
.socials{display:flex;gap:8px;margin-top:8px}
.socials span{width:15px;height:15px;border-radius:50%;background:var(--white)}
.globe{left:0;top:3142px;width:1200px;height:205px;background:linear-gradient(180deg,#0b1b33 0%,#17457a 50%,#2a6fa8 75%,#0e2d52 100%)}
.copyright{left:0;top:3252px;width:1200px;text-align:center;font-size:19px;font-weight:600;color:var(--white)}
.big-title{left:0;top:3450px;width:1200px;text-align:center;font-size:118px;font-weight:500;color:#222;letter-spacing:-1px}
</style>
</head>
<body>

<section class="abs hero">
  <nav class="abs nav">
    <a style="left:24px">REQUEST A QUOTE</a>
    <a style="left:154px">SIGNUP/LOGIN ⊙</a>
    <a style="left:288px">GET START</a>
    <svg style="position:absolute;left:387px;top:11px" width="17" height="17" viewBox="0 0 17 17"><circle cx="7" cy="7" r="5.5" fill="none" stroke="#1d1d1d" stroke-width="2"/><line x1="11" y1="11" x2="15.5" y2="15.5" stroke="#1d1d1d" stroke-width="2"/></svg>
    <div class="nav-right">
      <a style="left:45px">HOME</a>
      <a style="left:112px">SERVICES</a>
      <a class="active" style="left:185px">INDUSTRIES</a>
      <a style="left:282px">ABOUT US</a>
      <a style="left:370px">CONTACTUS</a>
    </div>
  </nav>
  <div class="abs brand"><span>TVAR<br>FREIGHT</span></div>
  <div class="abs submenu">
    <p>FOOD &amp; BEVERAGE</p><p>E-COMMERCE &amp; RETAIL</p><p>MANUFACTURING</p><p>PHARMA &amp; HEALTHCARE</p><p>GOVERNMENT</p>
  </div>
  <h1 class="abs page-title">FOOD &amp; BEVERAGE</h1>
  <div class="abs hero-photo" role="img" aria-label="Refrigerated box truck with open side showing fresh vegetables and fruit"></div>
  <p class="abs hero-copy">Tvar Freight provides reliable, compliant, and efficient trucking solutions for the food and beverage industry. We specialize in<br>transporting food products, beverages, ingredients, and packaged goods safely across regional and national routes while<br>maintaining strict quality and handling standards.</p>
</section>

<div class="abs cap" style="top:926px">
  <h2><em>OUR</em> CAPABILITIES</h2>
  <ul>
    <li>FULL TRUCKLOAD (FTL) &amp; LESS-THAN-TRUCKLOAD (LTL) SERVICES</li>
    <li>• TEMPERATURE-CONTROLLED &amp; REFRIGERATED FREIGHT (REEFER)</li>
    <li>• DRY VAN TRANSPORTATION FOR PACKAGED FOOD &amp; BEVERAGES</li>
    <li>• DISTRIBUTION CENTER &amp; RETAIL DELIVERIES</li>
    <li>• LONG-HAUL AND REGIONAL ROUTES</li>
    <li>• HIGH-VOLUME BEVERAGE SHIPMENTS</li>
    <li>• INGREDIENT &amp; RAW MATERIAL TRANSPORT</li>
  </ul>
</div>
<div class="abs cap" style="top:1089px">
  <h2><em>PRODUCTS WE</em> COMMONLY TRANSPORT</h2>
  <ul>
    <li>• BOTTLED AND CANNED BEVERAGES</li>
    <li>• DAIRY AND REFRIGERATED PRODUCTS</li>
    <li>• PACKAGED FOODS AND DRY GOODS</li>
    <li>• BULK INGREDIENTS AND RAW MATERIALS</li>
    <li>• ALCOHOL AND SPECIALTY BEVERAGES</li>
    <li>• RESTAURANT AND HOSPITALITY SUPPLIES</li>
  </ul>
</div>
<div class="abs cap" style="top:1243px">
  <h2><em>WHY CHOOSE</em> TVAR FREIGHT</h2>
  <ul>
    <li>• INDUSTRY-COMPLIANT FOOD TRANSPORTATION STANDARDS</li>
    <li>• EXPERIENCED CARRIERS FAMILIAR WITH FOOD HANDLING REQUIREMENTS</li>
    <li>• REAL-TIME TRACKING AND RELIABLE DELIVERY TIMELINES</li>
    <li>• FLEXIBLE CAPACITY FOR SEASONAL DEMAND SPIKES</li>
    <li>• COMPETITIVE PRICING AND SCALABLE LOGISTICS SOLUTIONS</li>
  </ul>
</div>

<div class="abs photo truck" role="img" aria-label="Trailer rear doors open with stacked cargo crates"></div>
<div class="abs photo shutter" role="img" aria-label="Trailer side curtain on a loading dock"></div>
<div class="abs photo drums-a" role="img" aria-label="Labelled drums on pallets"></div>
<div class="abs photo drums-b" role="img" aria-label="Drums lined up on a flatbed"></div>
<div class="abs photo loader" role="img" aria-label="Worker in high-visibility gear loading drums onto a truck"></div>

<section class="abs quote"></section>
<h2 class="abs quote-title">REQUEST A QUOTE</h2>
<div class="abs field" style="left:264px;top:1820px;width:340px">FIRT NAME</div>
<div class="abs field" style="left:623px;top:1820px;width:340px">LAST NAME</div>
<div class="abs field" style="left:264px;top:1891px;width:340px">EMAIL</div>
<div class="abs field" style="left:623px;top:1891px;width:340px">CONTACT NUMBER</div>

<div class="abs select" style="left:264px;top:1966px;width:222px">
  <div class="head">SHIPMENT TYPE<svg width="16" height="10" viewBox="0 0 16 10"><path d="M1 1 L8 8 L15 1" fill="none" stroke="#ef8560" stroke-width="2.5"/></svg></div>
  <div class="opt o1">AIR FREIGHT</div><div class="opt o2">OCEAN FREIGHT</div><div class="opt o3">GROUND</div><div class="opt o4">EXPRESS</div><div class="opt o2">WAREHOUSING</div>
</div>
<div class="abs select" style="left:502px;top:1966px;width:223px">
  <div class="head">PICKUP &amp; DELIVERY<svg width="16" height="10" viewBox="0 0 16 10"><path d="M1 1 L8 8 L15 1" fill="none" stroke="#ef8560" stroke-width="2.5"/></svg></div>
  <div class="opt o1">PICKUP COUNTRY / CITY</div><div class="opt o2">DELIVERY COUNTRY / CITY</div>
</div>
<div class="abs select" style="left:740px;top:1966px;width:223px">
  <div class="head">GOODS TYPE<svg width="16" height="10" viewBox="0 0 16 10"><path d="M1 1 L8 8 L15 1" fill="none" stroke="#ef8560" stroke-width="2.5"/></svg></div>
  <div class="opt o1">GENERAL</div><div class="opt o2">FRAGILE</div><div class="opt o3">PERISHABLE</div><div class="opt o4">HAZARDOUS</div><div class="opt o2">ELECTRONICS</div>
</div>
<div class="abs select" style="left:264px;top:2203px;width:340px">
  <div class="head">WEIGHT &amp; QUANTITY<svg width="16" height="10" viewBox="0 0 16 10"><path d="M1 1 L8 8 L15 1" fill="none" stroke="#ef8560" stroke-width="2.5"/></svg></div>
  <div class="opt o1">WEIGHT</div><div class="opt o2">NUMBER OF PACKAGES</div>
</div>
<div class="abs select" style="left:623px;top:2203px;width:340px">
  <div class="head">SERVICE LEVEL<svg width="16" height="10" viewBox="0 0 16 10"><path d="M1 1 L8 8 L15 1" fill="none" stroke="#ef8560" stroke-width="2.5"/></svg></div>
  <div class="opt o1">STANDARD</div><div class="opt o3">EXPRESS</div><div class="opt o2">PRIORITY</div>
</div>
<div class="abs message">MESSAGE</div>
<div class="abs cta">GET A QUOTE</div>

<p class="abs mission">OUR MISSION IS TO PROVIDE SAFE, DEPENDABLE TRANSPORTATION SERVICES THAT<br>KEEP FOOD AND BEVERAGE PRODUCTS MOVING EFFICIENTLY FROM PRODUCERS TO DISTRIBUTORS,<br>RETAILERS, AND CONSUMERS NATIONWIDE.</p>

<footer class="abs footer"></footer>
<div class="abs f-brand">TVAR<br>FREIGHT</div>
<p class="abs f-tag">READY TO MOVE YOUR<br>FREIGHT?</p>
<div class="abs f-col" style="left:425px;top:2941px">
  <h4>QUICK LINKS</h4><p>HOME</p><p>SERVICE</p><p>INDUSTRIES</p><p>REQUEST QUOTE</p><p>CONTACT US</p>
</div>
<div class="abs f-col" style="left:697px;top:2941px">
  <h4>SERVICES</h4><p>TRUCKLOAD FREIGHT</p><p>REEFER HAULING</p><p>DRY VAN</p><p>WAREHOUSING</p>
</div>
<div class="abs f-col f-contact" style="left:964px;top:2941px">
  <h4>CONTACT INFO</h4>
  <p>WE MOVE FREIGHT ACROSS REGIONAL AND NATIONAL ROUTES WITH CARE. REACH OUR TEAM ANY DAY FOR QUOTES, TRACKING AND SUPPORT ON EVERY SHIPMENT YOU BOOK.</p>
  <div class="phone">123-456-7890</div>
  <div class="socials"><span></span><span></span><span></span></div>
</div>
<div class="abs globe" role="img" aria-label="Night view of the globe with cargo ships and containers"></div>
<p class="abs copyright">© 2026. AN INDEPENDENT AGENT OF BRENNICK HAUL LLC.</p>

<h2 class="abs big-title">INDUSTRIES</h2>
</body>
</html>
```